Patient Satisfaction

We are extending our social listening and intelligence platform for Physicians to patient satisfaction app. Our platform monitors social media and review sites and collects, classifies and distilled patient satisfaction into nine Categories - Thoroughness, Answers Q's, Collaborative, Caring, Time Spent, Previous Success, Instruction Clarity, Follow-up and Reputation

The app will have three main states: (1) Home state showing the metric for each category, (2) a detailed page for each Category showing the metric, topics discussed and sites sourced, (3) Leaderboard showing Physicians with best scores.

If you follow our wireframes, please take liberty to extend it. We like the Lumora 6 tiles, but our wireframes fall far short of meeting its coolness and usefulness. For example, we don't have different size tiles, and would live them, or content on the tiles to make them more meaningful. [Note: use KT instead of KT.]
Updates

The designs submitted to date look great, but they reminded me that my instructions were unclear. Feel free to follow the wireframes if you like the UI, but we also welcome your thoughts on UI in addition to look and feel. If you follow our wireframes, please take liberty to extend it. We like the Lumora 6 tile, but our wireframes falls far short of meeting its coolness and usefulness. For example, we don't have different size tiles or content on the tiles to make them more meaningful. If you've submitted designs, please feel free to revise them or submit a different look. And if you haven't submitted designs, please feel free to give us your best thoughts on UI and design.

Target Market(s)

US Physicians

Industry/Entity Type

Media

Font styles to use
Sans Serif

Colors
f37022
5c5c5c
33a6d7

Requirements
Must have
• Home state
Visual icons
Nice to have
• Leaderbaord

```html
<!DOCTYPE html>
<html lang="en">
<head>
<meta charset="utf-8">
<title>Dashboard</title>
<link rel="stylesheet" href="https://fonts.googleapis.com/css2?family=Inter:wght@300;400;500&display=swap">
<style>
  :root {
    --bg-top: #7cbf2e;
    --bg-mid: #a6c93a;
    --bg-bottom: #bcdc8c;
    --white: #ffffff;
    --band: #f3f3f3;
    --ink: #222222;
    --label: #2a2a2a;
    --muted: #8a8a8a;
    --green: #1fb336;
    --blue: #1f8fe0;
    --orange: #f79a0e;
    --purple: #4a2c8f;
    --red: #e8262f;
    --gold: #f5bd0c;
  }
  * { box-sizing: border-box; margin: 0; padding: 0; }
  html, body { width: 676px; height: 1200px; overflow: hidden; }
  body {
    position: relative;
    font-family: "Inter", "Helvetica Neue", Arial, sans-serif;
    color: var(--ink);
  }
  .backdrop {
    position: absolute; inset: 0;
    background:
      radial-gradient(ellipse at 30% 55%, rgba(190,175,50,.55), transparent 60%),
      linear-gradient(170deg, var(--bg-top) 0%, var(--bg-mid) 50%, var(--bg-bottom) 100%);
  }
  .status-bar {
    position: absolute; top: 0; left: 0; width: 676px; height: 42px;
    display: flex; align-items: center; justify-content: space-between;
    padding: 0 12px; color: var(--white); font-size: 21px;
  }
  .status-left, .status-right { display: flex; align-items: center; gap: 8px; }
  .status-time { position: absolute; left: 0; right: 0; text-align: center; pointer-events: none; }
  .header-button {
    position: absolute; top: 99px; width: 93px; height: 93px; border-radius: 50%;
    background: var(--white); box-shadow: 0 3px 5px rgba(0,0,0,.2);
    display: flex; align-items: center; justify-content: center;
  }
  .menu-button { left: 22px; }
  .upload-button { left: 563px; }
  .title {
    position: absolute; top: 118px; left: 0; width: 676px; text-align: center;
    color: var(--white); font-weight: 300; font-size: 43px; letter-spacing: .5px;
  }
  .tile {
    position: absolute; width: 307px; height: 259px; background: var(--white);
    box-shadow: 0 2px 3px rgba(0,0,0,.18);
  }
  .tile-body { position: relative; height: 202px; display: flex; align-items: center; justify-content: center; }
  .tile-label {
    height: 57px; background: var(--band); display: flex; align-items: center; justify-content: center;
    font-size: 26px; font-weight: 500; color: var(--label); white-space: nowrap;
  }
  .col-1 { left: 21px; } .col-2 { left: 348px; }
  .row-1 { top: 287px; } .row-2 { top: 567px; } .row-3 { top: 847px; }
  .summary > * { position: absolute; left: 0; right: 0; display: flex; align-items: center; justify-content: center; }
  .score { top: 26px; height: 40px; font-size: 32px; font-weight: 400; }
  .rank { top: 81px; height: 44px; gap: 10px; color: var(--gold); font-size: 34px; }
  .comments { top: 156px; height: 26px; gap: 8px; color: var(--muted); font-size: 20px; }
</style>
</head>
<body>
  <div class="backdrop" role="img" aria-label="Soft green faceted background"></div>

  <div class="status-bar">
    <div class="status-left">
      <svg width="64" height="14" viewBox="0 0 64 14">
        <g fill="#fff"><circle cx="6" cy="7" r="5.5"/><circle cx="19" cy="7" r="5.5"/><circle cx="32" cy="7" r="5.5"/></g>
        <g fill="none" stroke="#fff" stroke-width="1.2"><circle cx="45" cy="7" r="5"/><circle cx="58" cy="7" r="5"/></g>
      </svg>
      <span>Carrio</span>
      <svg width="22" height="16" viewBox="0 0 22 16"><path d="M11 15 L2 5 A13 13 0 0 1 20 5 Z" fill="#fff"/></svg>
    </div>
    <div class="status-time">7:28 PM</div>
    <div class="status-right">
      <span>100%</span>
      <svg width="48" height="20" viewBox="0 0 48 20"><rect x="1" y="1" width="42" height="18" rx="3" fill="none" stroke="#fff" stroke-width="1.5"/><rect x="3.5" y="3.5" width="37" height="13" rx="1.5" fill="#fff"/><rect x="44" y="6" width="3" height="8" rx="1" fill="#fff"/></svg>
    </div>
  </div>

  <div class="header-button menu-button">
    <svg width="44" height="32" viewBox="0 0 44 32"><g stroke="var(--green)" stroke-width="4" stroke-linecap="round"><line x1="3" y1="4" x2="41" y2="4"/><line x1="3" y1="16" x2="41" y2="16"/><line x1="3" y1="28" x2="41" y2="28"/></g></svg>
  </div>
  <h1 class="title">DASHBOARD</h1>
  <div class="header-button upload-button">
    <svg width="50" height="46" viewBox="0 0 50 46" fill="none" stroke="var(--green)" stroke-width="3.5" stroke-linecap="round" stroke-linejoin="round">
      <path d="M16 33 H12 A9 9 0 0 1 11 15 A13 13 0 0 1 36 11 A11 11 0 0 1 38 33 H34"/>
      <line x1="25" y1="20" x2="25" y2="43"/><polyline points="18,27 25,20 32,27"/>
    </svg>
  </div>

  <section class="tile col-1 row-1">
    <div class="tile-body summary">
      <div class="score">KT: 72</div>
      <div class="rank">
        <svg width="40" height="40" viewBox="0 0 40 40"><circle cx="20" cy="20" r="17" fill="none" stroke="var(--gold)" stroke-width="4" stroke-dasharray="4 3"/><circle cx="20" cy="20" r="12" fill="var(--gold)"/><polygon points="20,12 22.4,17.6 28,18 23.6,21.6 25,27 20,24 15,27 16.4,21.6 12,18 17.6,17.6" fill="#fff"/></svg>
        <span>Rank 5 of 15</span>
      </div>
      <div class="comments">
        <svg width="26" height="24" viewBox="0 0 26 24"><path d="M1 1 H16 V11 H7 L3 15 V11 H1 Z" fill="#9a9a9a"/><path d="M8 8 H25 V19 H23 V23 L19 19 H8 Z" fill="#6f6f6f"/></svg>
        <span>14 Comments</span>
      </div>
    </div>
    <div class="tile-label">OverAll</div>
  </section>

  <section class="tile col-2 row-1">
    <div class="tile-body">
      <svg width="112" height="76" viewBox="0 0 112 76" fill="var(--green)"><rect x="0" y="0" width="5" height="76"/><rect x="0" y="44" width="112" height="5"/><rect x="107" y="36" width="5" height="40"/><circle cx="18" cy="34" r="7"/><rect x="30" y="31" width="78" height="9" rx="4"/></svg>
    </div>
    <div class="tile-label">Caring</div>
  </section>

  <section class="tile col-1 row-2">
    <div class="tile-body">
      <svg width="106" height="100" viewBox="0 0 106 100" fill="none" stroke="var(--blue)" stroke-width="4.5" stroke-linejoin="round">
        <path d="M9 10 H3 V88 H47 A6 6 0 0 0 59 88 H103 V10 H97"/>
        <path d="M53 16 C42 4 24 3 9 7 V80 C24 76 42 77 53 86 Z"/>
        <path d="M53 16 C64 4 82 3 97 7 V80 C82 76 64 77 53 86 Z"/>
      </svg>
    </div>
    <div class="tile-label">Thoroughness</div>
  </section>

  <section class="tile col-2 row-2">
    <div class="tile-body">
      <svg width="106" height="96" viewBox="0 0 106 96" fill="none" stroke="var(--orange)" stroke-width="4.5" stroke-linejoin="round">
        <path d="M8 3 H98 A5 5 0 0 1 103 8 V65 A5 5 0 0 1 98 70 H86 V92 L66 70 H8 A5 5 0 0 1 3 65 V8 A5 5 0 0 1 8 3 Z"/>
        <g fill="var(--orange)" stroke="none"><circle cx="39" cy="37" r="4"/><circle cx="53" cy="37" r="4"/><circle cx="67" cy="37" r="4"/></g>
      </svg>
    </div>
    <div class="tile-label">Answers Q's</div>
  </section>

  <section class="tile col-1 row-3">
    <div class="tile-body">
      <svg width="110" height="110" viewBox="0 0 110 110" fill="none" stroke="var(--purple)" stroke-width="4.5" stroke-linecap="round">
        <path d="M55 4 A50 50 0 1 1 23 16"/><line x1="55" y1="4" x2="55" y2="18"/>
        <line x1="32" y1="32" x2="55" y2="55" stroke-width="6"/><circle cx="55" cy="55" r="5" fill="var(--purple)" stroke="none"/>
      </svg>
    </div>
    <div class="tile-label">Time Spent</div>
  </section>

  <section class="tile col-2 row-3">
    <div class="tile-body">
      <svg width="118" height="100" viewBox="0 0 118 100" fill="none" stroke="var(--red)" stroke-width="4" stroke-linejoin="round" stroke-linecap="round">
        <path d="M16 42 C2 24 16 2 36 4 C46 5 53 11 59 20 C65 11 72 5 82 4 C102 2 116 24 102 42 L59 92 L28 56"/>
        <polyline points="2,50 30,50 38,34 46,66 52,40 58,54 62,48 80,48"/><circle cx="84" cy="48" r="3" fill="var(--red)"/>
      </svg>
    </div>
    <div class="tile-label">Previous Success</div>
  </section>
</body>
</html>
```